Fishing Tackle Product Packaging Backdrop/Template

Hi Designers,
we require a versatile packaging backdrop/template design for our fishing tackle brand. The design will be used in printed packaging for a range of products from small to large so would need to be scaleable. It will most commonly be used on small printed card tags (2x3"), but we would like to be able to use it for other packaging aswell.
A section for our product details, which we can edit ourselves would be essential, this way we can use the template for any of our products. The back of the card will need a space for our barcodes.
The design needs to be predominantly macsuline and appeal to the modern carp angler. It also needs to pop so that our goods really stand out against our competitors. Please see our logo attached. It'd also be great to see our web address at the bottom, on both sides of the design: www.brelvanrigs.co.uk

Thanks in advance and good luck!
Brelvan Rigs Team
Updates

Target Market(s)

Male Carp Anglers (aprox ages 18-60)

Industry/Entity Type

Fishing Tackle

Requirements
Must have
• Our logo and web address, with a section for a barcode and product title/info

```html
<!DOCTYPE html>
<html lang="en">
<head>
<meta charset="utf-8">
<title>Brelvan Rigs – Tackle Card Backdrop</title>
<link href="https://fonts.googleapis.com/css2?family=Oswald:wght@400;600&display=swap" rel="stylesheet">
<style>
  :root {
    --page-bg: #ffffff;
    --badge-green: #4a6b35;
    --badge-text: #ffffff;
    --swoosh-green: #8cc63f;
    --swoosh-yellow: #f2c313;
    --swoosh-blue: #3aa6c9;
    --lure-yellow: #e8b320;
    --lure-green: #4f9a3a;
    --lure-orange: #c9682a;
    --lure-blue: #3fa3d0;
    --lure-gold: #d7a21c;
    --lure-red: #e0452a;
    --wood-dark: #3b2f25;
    --info-panel: #ffffff;
    --info-title: #2f3b24;
    --info-text: #555555;
    --web-text: #ffffff;
  }
  html, body {
    margin: 0;
    width: 1200px;
    height: 1200px;
    overflow: hidden;
    background: var(--page-bg);
  }
  .canvas {
    position: relative;
    width: 1200px;
    height: 1200px;
  }
  .tag-card {
    position: absolute;
    left: 72px;
    top: 337px;
    width: 1056px;
    height: 528px;
  }
  .brand-name {
    font-family: "Oswald", sans-serif;
    font-weight: 600;
    font-size: 30px;
    fill: var(--badge-text);
    letter-spacing: 1px;
  }
  .product-title {
    font-family: "Oswald", sans-serif;
    font-weight: 600;
    font-size: 26px;
    fill: var(--info-title);
    letter-spacing: 1px;
  }
  .product-details {
    font-family: "Oswald", sans-serif;
    font-weight: 400;
    font-size: 17px;
    fill: var(--info-text);
  }
  .web-address {
    font-family: "Oswald", sans-serif;
    font-weight: 400;
    font-size: 20px;
    fill: var(--web-text);
    letter-spacing: 1px;
  }
</style>
</head>
<body>
<div class="canvas">
  <svg class="tag-card" viewBox="0 0 1100 550" xmlns="http://www.w3.org/2000/svg">
    <defs>
      <linearGradient id="lure-tones" x1="0" y1="0" x2="1" y2="0.35">
        <stop offset="0" stop-color="var(--lure-yellow)"/>
        <stop offset="0.2" stop-color="var(--lure-green)"/>
        <stop offset="0.42" stop-color="var(--lure-orange)"/>
        <stop offset="0.6" stop-color="var(--lure-blue)"/>
        <stop offset="0.8" stop-color="var(--lure-gold)"/>
        <stop offset="1" stop-color="var(--lure-red)"/>
      </linearGradient>
      <linearGradient id="wood-shade" x1="0" y1="0" x2="0" y2="1">
        <stop offset="0" stop-color="var(--wood-dark)" stop-opacity="0.15"/>
        <stop offset="0.6" stop-color="var(--wood-dark)" stop-opacity="0.35"/>
        <stop offset="1" stop-color="var(--wood-dark)" stop-opacity="0.85"/>
      </linearGradient>
      <linearGradient id="swoosh-fill" x1="0" y1="0" x2="1" y2="0">
        <stop offset="0" stop-color="var(--swoosh-green)"/>
        <stop offset="1" stop-color="var(--swoosh-yellow)"/>
      </linearGradient>
    </defs>

    <g class="lure-photo" role="img" aria-label="Photograph of colourful fishing lures laid side by side on a wooden table">
      <rect width="1100" height="550" fill="url(#lure-tones)"/>
      <rect width="1100" height="550" fill="url(#wood-shade)"/>
    </g>

    <g class="corner-swoosh">
      <path d="M0,0 H565 C480,45 300,100 0,118 Z" fill="var(--swoosh-blue)"/>
      <path d="M0,0 H548 C462,38 292,88 0,104 Z" fill="#ffffff" opacity="0.85"/>
      <path d="M0,0 H540 C455,34 288,82 0,98 Z" fill="url(#swoosh-fill)"/>
    </g>

    <g class="brand-badge">
      <circle cx="311" cy="271" r="102" fill="var(--badge-green)"/>
      <text class="brand-name" x="311" y="282" text-anchor="middle">Brelvan Rigs</text>
    </g>

    <g class="product-info">
      <rect class="product-info-panel" x="725" y="340" width="310" height="151" fill="var(--info-panel)"/>
      <text class="product-title" x="745" y="385">PRODUCT TITLE</text>
      <text class="product-details" x="745" y="420">Size / weight: 00g</text>
      <text class="product-details" x="745" y="446">Quantity: 00 per pack</text>
      <text class="product-details" x="745" y="472">Product code: 0000</text>
    </g>

    <text class="web-address" x="550" y="532" text-anchor="middle">www.brelvanrigs.co.uk</text>
  </svg>
</div>
</body>
</html>
```